KELPO's Coffee Liqueur Shot Arabica

Need a lable for a 500ml bottle of homemade Coffee liqueur.
Name:
KELPO's
Coffee
Shot

Shape: Round, 80mm
Color of the lable should be black and letters in black.
Letters KELPO's min 12mm hight.
Color of the liqueur is dark brown.
Add: 500ml
Add: 38% vol.
Should have a bean on the lable.
Maybe some bullet words on the bottom...
Prefered design see Pic1a with bottle.

Target Market(s)

People that enjoy coffee in shots, in coctails, with ice or on top of icecream or any other dessert

Font styles to use
Serif

Colors

Designer to choose colors to be used in the design.

Requirements
Must have
• See Pic 1a
Nice to have
• See Pic1a (bottle)
Should not have
• Different colors

```html
<!DOCTYPE html>
<html lang="en">
<head>
<meta charset="utf-8">
<title>KELPO's Coffee Shot – Round Label</title>
<link rel="stylesheet" href="https://fonts.googleapis.com/css2?family=Abril+Fatface&family=Black+Ops+One&family=Big+Shoulders+Display:wght@800&family=Oswald:wght@500&display=swap">
<style>
  :root {
    --ink: #0d0d0d;
    --paper: #ffffff;
    --backdrop: #200e0d;
  }
  html, body {
    margin: 0;
    padding: 0;
    width: 1188px;
    height: 1200px;
    overflow: hidden;
    background: var(--backdrop);
  }
  .label {
    display: block;
    width: 1188px;
    height: 1200px;
  }
  .label-disc { fill: var(--paper); }
  .label-ring { fill: none; stroke: var(--ink); stroke-width: 6; }
  .rule { fill: none; stroke: var(--ink); stroke-width: 8; stroke-linecap: butt; }
  .rule-thin { fill: none; stroke: var(--ink); stroke-width: 3; }
  .dotted-ring { fill: none; stroke: var(--ink); stroke-width: 2; stroke-dasharray: 2 5; }
  .brand-name {
    font-family: "Black Ops One", serif;
    font-size: 196px;
    fill: var(--ink);
    text-transform: uppercase;
  }
  .product-name {
    font-family: "Abril Fatface", serif;
    font-size: 178px;
    fill: var(--ink);
    text-anchor: middle;
  }
  .spec {
    font-family: "Oswald", sans-serif;
    font-weight: 500;
    font-size: 42px;
    letter-spacing: 3px;
    fill: var(--ink);
  }
  .tagline {
    font-family: "Big Shoulders Display", sans-serif;
    font-weight: 800;
    font-size: 74px;
    letter-spacing: 6px;
    fill: var(--ink);
    text-anchor: middle;
  }
  .bean-badge-ring { fill: none; stroke: var(--ink); stroke-width: 4; }
  .bean-badge { fill: var(--ink); }
</style>
</head>
<body>
<svg class="label" viewBox="0 0 1188 1200" xmlns="http://www.w3.org/2000/svg">
  <defs>
    <path id="arc-top" d="M 219 600 A 375 375 0 0 1 969 600"/>
    <path id="arc-bottom" d="M 112 600 A 482 482 0 0 0 1076 600"/>
  </defs>

  <circle class="label-disc" cx="594" cy="600" r="575"/>
  <circle class="label-ring" cx="594" cy="600" r="545"/>

  <text class="brand-name">
    <textPath href="#arc-top" startOffset="50%" text-anchor="middle" textLength="820" lengthAdjust="spacingAndGlyphs">KELPO's</textPath>
  </text>

  <path class="dotted-ring" d="M 417 423 A 250 250 0 0 1 771 423"/>
  <path class="dotted-ring" d="M 355 690 A 255 255 0 0 0 833 690"/>

  <line class="rule" x1="77" y1="498" x2="270" y2="498"/>
  <line class="rule" x1="904" y1="498" x2="1102" y2="498"/>

  <text class="product-name" x="594" y="512">Coffee</text>
  <text class="product-name" x="594" y="650">Shot</text>

  <text class="spec" x="75" y="616">38% VOL.</text>
  <line class="rule-thin" x1="282" y1="594" x2="362" y2="594"/>
  <line class="rule-thin" x1="312" y1="604" x2="362" y2="604"/>

  <text class="spec" x="1110" y="616" text-anchor="end">500ML</text>
  <line class="rule-thin" x1="826" y1="594" x2="906" y2="594"/>
  <line class="rule-thin" x1="826" y1="604" x2="876" y2="604"/>

  <path class="rule" d="M 77 697 H 285 A 324 324 0 0 0 386 848"/>
  <path class="rule" d="M 1102 697 H 903 A 324 324 0 0 1 802 848"/>

  <circle class="bean-badge-ring" cx="594" cy="834" r="146"/>
  <circle class="bean-badge" cx="594" cy="834" r="132" role="img" aria-label="Coffee bean emblem"/>

  <text class="tagline">
    <textPath href="#arc-bottom" startOffset="24%">ARABICA</textPath>
  </text>
  <text class="tagline">
    <textPath href="#arc-bottom" startOffset="76%">INTENSIV</textPath>
  </text>
</svg>
</body>
</html>
```